Re-vamp existing website :www.tallowmerefinch.com.au

We need a new website design for this website
www.tallowmerefinch.com.au.

"creating financial lightbulb moments"

Looking for something modern, corporate like this https://www.pebbleharbor.com.au

Imagery is important, showing really great images of what we do.

We want to keep the theme of:
Build Your Future
Invest in your Dreams
Grow You

We want a blog/opinion page on the website

Staying with our three logo colours throughout

Industry/Entity Type

Financial Service

Number of Pages Required

5+ page

```html
<!DOCTYPE html>
<html lang="en">
<head>
<meta charset="utf-8">
<title>Tallowmere Finch – Build Your Future</title>
<link href="https://fonts.googleapis.com/css2?family=Open+Sans:wght@400;600;700;800&display=swap" rel="stylesheet">
<style>
:root{
  --green:#8dc63f;
  --green-dark:#76ad2c;
  --blue:#1a8ed1;
  --blue-dark:#1479b5;
  --navy:#1f3a57;
  --ink:#333a40;
  --muted:#6b7278;
  --band:#eef0f1;
  --white:#ffffff;
  --line:#dfe3e6;
}
*{box-sizing:border-box;margin:0;padding:0}
html,body{width:735px;height:1200px;overflow:hidden}
body{font-family:"Open Sans",Arial,sans-serif;color:var(--ink);background:var(--white);position:relative}
.site-header{height:85px;display:flex;align-items:center;justify-content:space-between;padding:0 30px 0 30px}
.brand{display:flex;align-items:center;gap:8px}
.brand-dot{width:22px;height:22px;border-radius:50%;background:var(--green)}
.brand-name{font-size:15px;font-weight:700;color:var(--blue);line-height:1.05;width:90px}
.main-nav{display:flex;align-items:center;gap:26px;font-size:10px;font-weight:600;color:var(--ink);text-transform:uppercase}
.main-nav .active{color:var(--green)}
.search-btn{width:26px;height:26px;border-radius:50%;background:var(--green);display:flex;align-items:center;justify-content:center}
.hero{position:relative;height:320px;overflow:hidden}
.hero-photo{position:absolute;inset:0;background:linear-gradient(90deg,#e9e9e7 0%,#d9d9d6 45%,#b9bbb8 75%,#a9c08a 100%)}
.hero-copy{position:absolute;left:30px;top:95px}
.hero-title{font-size:52px;font-weight:800;line-height:1;color:var(--navy);letter-spacing:-0.5px;text-transform:uppercase}
.btn{display:inline-block;background:var(--green);color:var(--white);font-size:10px;font-weight:700;text-transform:uppercase;padding:9px 18px;border-radius:2px}
.hero .btn{margin-top:22px}
.hero-dots{position:absolute;bottom:14px;left:50%;transform:translateX(-50%);display:flex;gap:7px}
.hero-dots span{width:7px;height:7px;border-radius:50%;background:#fff;opacity:.7}
.hero-dots span.on{opacity:1;background:var(--green)}
.journey{text-align:center;padding:30px 80px 0}
.section-title{font-size:19px;font-weight:700;color:var(--blue);text-transform:uppercase}
.journey p{font-size:10.5px;line-height:1.65;color:var(--muted);margin:14px auto 20px;max-width:560px}
.steps-band{position:absolute;top:600px;left:0;width:735px;height:210px;background:var(--band)}
.step-card{position:absolute;top:30px;width:155px;height:132px;background:var(--white);border-bottom:3px solid var(--green);text-align:center;padding-top:22px}
.step-card svg{display:block;margin:0 auto 12px}
.step-card h3{font-size:10px;font-weight:600;color:var(--blue);line-height:1.4;padding:0 12px}
.steps-band .btn{position:absolute;left:50%;transform:translateX(-50%);top:188px;white-space:nowrap}
.partners{position:absolute;top:850px;left:0;width:735px;height:120px}
.partner-row{position:absolute;left:40px;width:655px;display:flex;justify-content:space-between}
.partner-badge{width:56px;height:28px;border-radius:3px;background:#d7dde3}
.partner-badge.b{background:#c9d9ea}.partner-badge.g{background:#d6e6c5}.partner-badge.r{background:#ead3d3}
.partner-arrow{position:absolute;top:50px}
.site-footer{position:absolute;top:990px;left:0;width:735px;height:185px;background:var(--blue);color:var(--white);padding:22px 30px 0;display:flex;gap:30px}
.footer-col h4{font-size:11px;font-weight:700;text-transform:uppercase;margin-bottom:10px}
.footer-col p,.footer-col li{font-size:9px;line-height:1.65;list-style:none;opacity:.92}
.col-about{width:190px}.col-map{width:115px}.col-contact{width:155px}
.award{display:flex;gap:10px;align-items:flex-start;width:140px}
.award-badge{width:52px;height:52px;border-radius:50%;background:#f3c325;flex:none}
.award p{font-size:9px;font-weight:700;line-height:1.45}
.footer-bar{position:absolute;top:1175px;left:0;width:735px;height:25px;background:var(--blue-dark);color:var(--white);display:flex;align-items:center;justify-content:space-between;padding:0 30px;font-size:8.5px}
.social{display:flex;gap:6px}
.social span{width:13px;height:13px;background:rgba(255,255,255,.85);border-radius:2px}
</style>
</head>
<body>
<header class="site-header">
  <div class="brand"><span class="brand-dot"></span><span class="brand-name">Tallowmere Finch</span></div>
  <nav class="main-nav">
    <span class="active">Home</span><span>About Us</span><span>Home Loans</span><span>Business Lending</span><span>Contact Us</span>
    <span class="search-btn"><svg width="12" height="12" viewBox="0 0 12 12"><circle cx="5" cy="5" r="3.6" fill="none" stroke="#fff" stroke-width="1.6"/><line x1="7.7" y1="7.7" x2="11" y2="11" stroke="#fff" stroke-width="1.6"/></svg></span>
  </nav>
</header>

<section class="hero">
  <div class="hero-photo" role="img" aria-label="Businessman watering green grass steps rising along a concrete wall"></div>
  <div class="hero-copy">
    <h1 class="hero-title">Build Your<br>Future</h1>
    <a class="btn">Read More</a>
  </div>
  <div class="hero-dots"><span class="on"></span><span></span><span></span><span></span></div>
</section>

<section class="journey">
  <h2 class="section-title">How Your TF Journey Works</h2>
  <p>Tallowmere Finch (TF) is a leading Australian finance brokerage group dedicated to providing our clients with a range of financial solutions tailored to their individual requirements. We want our clients to be bold in chasing their financial dreams and we commit to provide a range of opportunities for them to do so. Tallowmere Finch aims to push the status quo by doing things differently.</p>
  <a class="btn">Read More</a>
</section>

<section class="steps-band">
  <div class="step-card" style="left:44px">
    <svg width="34" height="30" viewBox="0 0 34 30"><rect x="2" y="4" width="24" height="24" rx="2" fill="none" stroke="#6b7278" stroke-width="2"/><path d="M14 18 L29 3 L32 6 L17 21 L13 22 Z" fill="#6b7278"/></svg>
    <h3>Our TF Mapping Session - Identifying your Ideas &amp; Goals</h3>
  </div>
  <div class="step-card" style="left:215px">
    <svg width="34" height="30" viewBox="0 0 34 30"><rect x="2" y="2" width="30" height="26" fill="none" stroke="#6b7278" stroke-width="2"/><rect x="8" y="16" width="4" height="8" fill="#6b7278"/><rect x="15" y="11" width="4" height="13" fill="#6b7278"/><rect x="22" y="7" width="4" height="17" fill="#6b7278"/></svg>
    <h3>Structure &amp;<br>Strategy</h3>
  </div>
  <div class="step-card" style="left:387px">
    <svg width="34" height="30" viewBox="0 0 34 30"><path d="M11 13 V9 a6 6 0 0 1 12 0 V13" fill="none" stroke="#6b7278" stroke-width="2.5"/><rect x="7" y="13" width="20" height="15" rx="2" fill="#6b7278"/></svg>
    <h3>Protect</h3>
  </div>
  <div class="step-card" style="left:558px">
    <svg width="34" height="30" viewBox="0 0 34 30"><path d="M7 15 a10 10 0 0 1 18 -6" fill="none" stroke="#8dc63f" stroke-width="3"/><path d="M27 15 a10 10 0 0 1 -18 6" fill="none" stroke="#8dc63f" stroke-width="3"/><path d="M21 4 L27 9 L20 11 Z" fill="#8dc63f"/><path d="M13 26 L7 21 L14 19 Z" fill="#8dc63f"/></svg>
    <h3>Implementation &amp;<br>Review</h3>
  </div>
  <a class="btn">Click Here to Start Your Journey</a>
</section>

<section class="partners" aria-label="Lending partners">
  <svg class="partner-arrow" style="left:12px" width="10" height="14" viewBox="0 0 10 14"><path d="M8 1 L2 7 L8 13" fill="none" stroke="#555" stroke-width="2"/></svg>
  <div class="partner-row" style="top:18px">
    <span class="partner-badge b"></span><span class="partner-badge g"></span><span class="partner-badge b"></span><span class="partner-badge b"></span><span class="partner-badge b"></span><span class="partner-badge"></span><span class="partner-badge g"></span><span class="partner-badge"></span><span class="partner-badge r"></span><span class="partner-badge r"></span>
  </div>
  <div class="partner-row" style="top:60px">
    <span class="partner-badge b"></span><span class="partner-badge g"></span><span class="partner-badge b"></span><span class="partner-badge r"></span><span class="partner-badge g"></span><span class="partner-badge b"></span><span class="partner-badge"></span><span class="partner-badge r"></span><span class="partner-badge b"></span><span class="partner-badge b"></span>
  </div>
  <svg class="partner-arrow" style="left:713px" width="10" height="14" viewBox="0 0 10 14"><path d="M2 1 L8 7 L2 13" fill="none" stroke="#555" stroke-width="2"/></svg>
</section>

<footer class="site-footer">
  <div class="footer-col col-about">
    <h4>About Us</h4>
    <p>At Tallowmere Finch our team works with you to plan, build and grow a secure financial future for you and your family.</p>
    <p style="margin-top:8px">Note: All advice is general in nature only.</p>
  </div>
  <div class="footer-col col-map">
    <h4>Site Map</h4>
    <ul><li>Home</li><li>About Us</li><li>Home Loans</li><li>Business Lending</li><li>Contact Us</li></ul>
  </div>
  <div class="footer-col col-contact">
    <h4>Contact Details</h4>
    <p>Suite 4, Level 2<br>18 Harbour View Road<br>Perth WA 6000</p>
    <p style="margin-top:6px">0400 000 000<br>info@tallowmerefinch.com.au</p>
  </div>
  <div class="award">
    <span class="award-badge"></span>
    <p>Lending Review Top 30 Rising Brokers in Australia</p>
  </div>
</footer>
<div class="footer-bar">
  <span>Copyright 2016 Tallowmere Finch. All Rights Reserved.</span>
  <span class="social"><span></span><span></span><span></span><span></span></span>
</div>
</body>
</html>
```